Maple Crest Holdings Inc.
Professional
Simon Oduya
Director
Lot 24 Hibiscus Lane Tremont,
Georgetown, Guyana
simon_d_oduya@mailnest-example.com
www.mchi-example.com
Logo and website

```html
<!DOCTYPE html>
<html lang="en">
<head>
<meta charset="utf-8">
<title>Maple Crest Holdings Inc. — Stationery</title>
<link href="https://fonts.googleapis.com/css2?family=Montserrat:wght@400;600;700&display=swap" rel="stylesheet">
<style>
  :root{
    --backdrop:#5b5e62;
    --paper:#ffffff;
    --navy:#1d2f6b;
    --red:#c62026;
    --ink:#2a2f3a;
    --muted:#8a8f99;
    --ghost:#eceef3;
  }
  *{margin:0;padding:0;box-sizing:border-box}
  html,body{width:1200px;height:310px;overflow:hidden}
  body{background:var(--backdrop);font-family:"Montserrat",Arial,sans-serif;position:relative;color:var(--ink)}
  .piece{position:absolute;background:var(--paper);overflow:hidden;box-shadow:0 2px 6px rgba(0,0,0,.35)}
  .brand{display:flex;align-items:center;gap:4px;font-weight:700;color:var(--navy);white-space:nowrap}
  .brand .dot{border-radius:50%;background:var(--navy);flex:none}
  .waves{position:absolute;left:0;bottom:0;width:100%}
  .ghost-mark{position:absolute;border-radius:50%;background:var(--ghost)}
  .contact{position:absolute;font-size:4.2px;line-height:1.45;color:var(--muted);text-align:right}

  /* logo presentation */
  .logo-sheet{left:24px;top:12px;width:132px;height:72px;background:#3f4246;box-shadow:none;display:flex;align-items:center;justify-content:center}
  .logo-sheet .brand{color:#fff;font-size:7.5px}
  .logo-sheet .brand .dot{width:14px;height:14px;background:var(--red)}

  /* business cards */
  .card-front{left:24px;top:228px;width:125px;height:65px;display:flex;align-items:center;justify-content:center}
  .card-front .brand{font-size:6px}
  .card-front .brand .dot{width:10px;height:10px}
  .card-back{left:156px;top:228px;width:125px;height:65px;background:var(--navy);display:flex;align-items:center;justify-content:center}
  .card-back .brand{color:#fff;font-size:6px}
  .card-back .brand .dot{width:10px;height:10px;background:var(--red)}

  /* letterheads */
  .letterhead{top:19px;width:190px;height:274px}
  .letterhead.one{left:284px}
  .letterhead.two{left:490px}
  .letterhead .brand{position:absolute;left:12px;top:12px;font-size:5.5px}
  .letterhead .brand .dot{width:11px;height:11px}
  .letterhead .contact{right:12px;top:13px}
  .letterhead .ghost-mark{left:65px;top:95px;width:60px;height:60px}

  /* compliment / envelope fronts */
  .dl{left:696px;width:223px;height:88px}
  .dl.upper{top:108px}
  .dl.lower{top:211px}
  .dl .brand{position:absolute;left:10px;top:10px;font-size:5px}
  .dl .brand .dot{width:9px;height:9px}
  .dl .contact{right:10px;top:11px}
  .dl .ghost-mark{left:94px;top:22px;width:36px;height:36px}

  /* envelope backs */
  .env{left:943px;width:233px;height:80px;background:var(--paper)}
  .env.red{top:19px}
  .env.navy{top:113px}
  .env.plain{top:207px}
  .env .flap{position:absolute;left:0;top:0;width:100%;height:100%}
</style>
</head>
<body>

  <div class="piece logo-sheet">
    <div class="brand"><span class="dot"></span>Maple Crest Holdings Inc.</div>
  </div>

  <div class="piece card-front">
    <div class="brand"><span class="dot"></span>Maple Crest Holdings Inc.</div>
    <svg class="waves" viewBox="0 0 125 14" preserveAspectRatio="none" height="14">
      <path d="M0 8 C40 2 80 12 125 5 L125 14 L0 14Z" fill="var(--navy)"/>
      <path d="M0 6 C40 0 80 10 125 3 L125 5 C80 12 40 2 0 8Z" fill="var(--red)"/>
    </svg>
  </div>

  <div class="piece card-back">
    <div class="brand"><span class="dot"></span>Maple Crest Holdings Inc.</div>
  </div>

  <div class="piece letterhead one">
    <div class="brand"><span class="dot"></span>Maple Crest Holdings Inc.</div>
    <p class="contact">Simon Oduya, Director<br>Lot 24 Hibiscus Lane Tremont<br>Georgetown, Guyana<br>simon_d_oduya@mailnest-example.com<br>www.mchi-example.com</p>
    <span class="ghost-mark"></span>
    <svg class="waves" viewBox="0 0 190 24" preserveAspectRatio="none" height="24">
      <path d="M0 14 C60 4 120 22 190 8 L190 24 L0 24Z" fill="var(--navy)"/>
      <path d="M0 11 C60 1 120 19 190 5 L190 8 C120 22 60 4 0 14Z" fill="var(--red)"/>
    </svg>
  </div>

  <div class="piece letterhead two">
    <div class="brand"><span class="dot"></span>Maple Crest Holdings Inc.</div>
    <span class="ghost-mark"></span>
    <svg class="waves" viewBox="0 0 190 24" preserveAspectRatio="none" height="24">
      <path d="M0 14 C60 4 120 22 190 8 L190 24 L0 24Z" fill="var(--navy)"/>
      <path d="M0 11 C60 1 120 19 190 5 L190 8 C120 22 60 4 0 14Z" fill="var(--red)"/>
    </svg>
  </div>

  <div class="piece dl upper">
    <div class="brand"><span class="dot"></span>Maple Crest Holdings Inc.</div>
    <p class="contact">Lot 24 Hibiscus Lane Tremont<br>Georgetown, Guyana<br>www.mchi-example.com</p>
    <span class="ghost-mark"></span>
    <svg class="waves" viewBox="0 0 223 14" preserveAspectRatio="none" height="14">
      <path d="M0 8 C70 2 150 12 223 4 L223 14 L0 14Z" fill="var(--navy)"/>
      <path d="M0 6 C70 0 150 10 223 2 L223 4 C150 12 70 2 0 8Z" fill="var(--red)"/>
    </svg>
  </div>

  <div class="piece dl lower">
    <div class="brand"><span class="dot"></span>Maple Crest Holdings Inc.</div>
    <span class="ghost-mark"></span>
    <svg class="waves" viewBox="0 0 223 14" preserveAspectRatio="none" height="14">
      <path d="M0 8 C70 2 150 12 223 4 L223 14 L0 14Z" fill="var(--navy)"/>
      <path d="M0 6 C70 0 150 10 223 2 L223 4 C150 12 70 2 0 8Z" fill="var(--red)"/>
    </svg>
  </div>

  <div class="piece env red">
    <svg class="flap" viewBox="0 0 233 80" preserveAspectRatio="none">
      <path d="M0 0 H233 V12 L116.5 48 L0 12Z" fill="var(--red)"/>
      <circle cx="116.5" cy="40" r="6" fill="var(--paper)"/>
    </svg>
  </div>

  <div class="piece env navy">
    <svg class="flap" viewBox="0 0 233 80" preserveAspectRatio="none">
      <path d="M0 0 H233 V12 L116.5 48 L0 12Z" fill="var(--navy)"/>
      <circle cx="116.5" cy="40" r="6" fill="var(--paper)"/>
    </svg>
  </div>

  <div class="piece env plain">
    <svg class="flap" viewBox="0 0 233 80" preserveAspectRatio="none">
      <path d="M0 0 H233 V8 L116.5 44 L0 8Z" fill="#f4f5f7" stroke="#d9dce2" stroke-width="0.6"/>
      <path d="M0 0 H233 V4 L116.5 40 L0 4Z" fill="none" stroke="var(--red)" stroke-width="2"/>
    </svg>
  </div>

</body>
</html>
```